Vast Ledger Web Design - For local online shopping 'village'

URGENTLY REQUIRE WEB DESIGNER FOR VAST LEDGER WEB STORE - CODING REQUIRED

REQUIREMENT; BE ABLE TO TALK ENGLISH VERY WELL AS THIS WILL BE AN ON GOING PROJECT

(WE WILL BE TALKING ON TALKLOOM OR CHIRPLINE)

The business name is 'Holmwyck's - Corvale's Online Shopping Village'
(PICS ATTACHED FOR LAYOUT DEMONSTRATION PURPOSES)

I need a draft of the website operational within 7 days to show potential clients. The remainder may take an additional 7+ days to complete. Can discuss further payments due to the work involved.

It's an online shopping village where individual shop owners have the ability to place their store (logo) and their products on this website to increase exposure to their business and more importantly their online delivery service.

The site will need to be structured in a very easy to use manner. Customers ages will range from 18+ to 80+.

THE IMAGINATION, FEEL & PRESENCE OF THE WEB PAGE;
You are a professional web designer, I will need you to use your imagination and add pieces to this website that I can't see. My vision and feel for this website is based on the grocery stores that were able to survive and thrive during the late stages of WWII. A lot of design now and with future marketing & advertising will be revolved and the 1940's feel & look. I'm happy to hear your thoughts on things we can add or improve on in the site. It's very basic now and it's more warmth and character.

THE LAYOUT;
The first page will have a white brick wallpaper background (pic attached as 'wallpaper'. This will be the wallpaper used for the entire site. The business logo (hasn't been made yet - waiting on drafts) will be at the top of the page and beneath it will be 3 categories to choose from (in the final stage it will have 6 categories).

DRAFT STAGE;
1. Village grocers (pic attached ' vgrocers') (To be written ' Village Grocers written on the frame burnt into the wood or written underneath the frame - must be large and clear to read')
2. Butchers (pic attached 'vbutcher')(as above - Village butchers)
3. Seafood (pic attached 'VSF')(as above Seafood)
They will all require framing (pic attached 'frame')
I'd like the images to be slightly bouncy if you put your mouse or finger on the logo.

Once the customer enters their choice it will then take them to their desired category.

NEXT PAGE:

Main focus is in the Grocers section; The same design structure will appear (business logo 'Holmwyck - Corvale's online shopping village'.
2 business choices will be available in this section. Their logos are attached ('PDNQ' and 'Mundey's Grocer') I'd like you to enhance the logo's with more depth and background shadow - please don't spend to much time but make them look better. I'd like the logo's to be slightly bouncy if you put your mouse or finger on the logo. The wallpaper used will be 'wallpaper'.

PLEASE NOTE: Could you please remove the logo from the background image of 'PDNQ'.

For the draft stage we will focus on 'PDNQ'. Once you click on PDNQ it will take you to their page. The wallpaper will be the same as the brick wallpaper on the other 2 pages. The logo of 'PDNQ' will be placed boldly at the top middle of the page. On this page there will be 4 categories to choose from. Everything will be the same, wallpaper will be white brick, the categories (pics attached as Deli, Fruit&Veg, Bakery & Pantry ) they will need to be framed and the category name will be burnt into the wood or placed underneath.

This is where we stop for the time being.

I've attached layout pictures, so you can see what I see. Please add all the little things i've added to the layout pictures that i haven't written here..

Example: Our Mission, Contact us, Home delivery.. etc.

The site will need to continue to grow as we fill the categories with products and add more businesses to the site.. so on and so on. It's an ongoing job and we will need good communication and understanding with each other.

Please do what you can to show your vision in line with what i've written above. If you'd like to contact me feel free to do so, we can organize a talk on talkloom if need be.

All the best & I hope you are all safe and healthy!

Odo

Industry/Entity Type

Online Store

Coding

Coded - Design and coding required

Number of Pages Required

5+ page

Requirements
Must have
• Looks like the 1940's merged with the modern age.
Nice to have
• Age some nice grocery store touches. 1940's + grocery stores had things hanging from the walls, ornaments here and there. It felt homely. Add some things or talk about the things that you're thinking about adding.

```html
<!DOCTYPE html>
<html lang="en">
<head>
<meta charset="utf-8">
<title>Holmwyck – Corvale's Online Shopping Village</title>
<link href="https://fonts.googleapis.com/css2?family=Barlow:wght@400;500;600;700&family=Barlow+Condensed:wght@500;600;700&display=swap" rel="stylesheet">
<style>
  :root {
    --ink: #111111;
    --text: #333333;
    --muted: #8a8a8a;
    --white: #ffffff;
    --rule: #e3e3e3;
    --brick-light: #f1f1f0;
    --brick-mid: #dedcda;
    --footer: #151515;
    --overlay: rgba(60, 42, 28, 0.62);
    --wood-dark: #4a2c16;
    --wood: #7a4a25;
  }
  * { box-sizing: border-box; margin: 0; padding: 0; }
  html, body { width: 1200px; height: 2193px; overflow: hidden; background: var(--white); }
  body { font-family: "Barlow", sans-serif; color: var(--text); position: relative; }
  .abs { position: absolute; }

  /* Header */
  .site-header { position: absolute; left: 0; top: 0; width: 1200px; height: 175px; background: var(--white); border-bottom: 1px solid var(--rule); }
  .brand { position: absolute; left: 76px; top: 52px; width: 250px; text-align: center; font-family: "Barlow Condensed", sans-serif; font-weight: 700; color: var(--ink); }
  .brand-name { font-size: 40px; line-height: 40px; letter-spacing: 1px; }
  .brand-tag { font-size: 17px; line-height: 22px; margin-top: 2px; letter-spacing: 0.2px; }
  .search { position: absolute; left: 386px; top: 69px; width: 466px; height: 46px; border: 1px solid #d6d6d6; display: flex; align-items: center; padding-left: 18px; }
  .search span { margin-left: 20px; font-size: 14px; color: var(--muted); }
  .account { position: absolute; left: 875px; top: 80px; display: flex; align-items: center; gap: 10px; font-size: 16px; color: var(--ink); }
  .cart { position: absolute; left: 1076px; top: 83px; display: flex; align-items: center; gap: 6px; font-family: Georgia, serif; font-size: 16px; color: var(--ink); }

  /* Nav */
  .main-nav { position: absolute; left: 0; top: 175px; width: 1200px; height: 68px; background: var(--white); }
  .main-nav a { position: absolute; top: 24px; font-size: 18px; color: var(--ink); text-decoration: none; }

  /* Hero */
  .hero { position: absolute; left: 0; top: 243px; width: 1200px; height: 537px; background: radial-gradient(ellipse at 65% 45%, #b07a45 0%, #7a4d28 40%, #3e2714 100%); }
  .hero-panel { position: absolute; left: 104px; top: 99px; width: 497px; height: 310px; background: var(--overlay); }
  .hero-title { position: absolute; left: 51px; top: 34px; font-size: 54px; font-weight: 700; color: var(--white); letter-spacing: 0.5px; line-height: 60px; }
  .hero-sub { position: absolute; left: 57px; top: 96px; font-family: "Barlow Condensed", sans-serif; font-weight: 600; font-size: 20px; color: var(--white); }
  .hero-copy { position: absolute; left: 55px; top: 136px; width: 400px; font-size: 14px; line-height: 22px; color: var(--white); }
  .btn-outline { position: absolute; left: 56px; top: 222px; width: 159px; height: 41px; border: 2px solid var(--white); color: var(--white); font-family: "Barlow Condensed", sans-serif; font-weight: 700; font-size: 18px; display: flex; align-items: center; justify-content: center; }
  .hero-arrow { position: absolute; top: 248px; width: 37px; height: 42px; background: rgba(0,0,0,0.45); display: flex; align-items: center; justify-content: center; }

  /* Brick area */
  .brick-wall { position: absolute; left: 0; top: 780px; width: 1200px; height: 1228px; background: linear-gradient(180deg, var(--brick-light) 0%, var(--brick-mid) 50%, var(--brick-light) 100%); }

  .category { position: absolute; top: 847px; width: 327px; }
  .frame { width: 327px; height: 251px; border: 42px solid var(--wood); border-left-width: 46px; border-right-width: 46px; background: #333; box-shadow: 0 4px 8px rgba(0,0,0,0.35); outline: 4px solid var(--wood-dark); outline-offset: -4px; }
  .frame .photo { width: 100%; height: 100%; }
  .category-label { position: absolute; top: 274px; left: 0; width: 327px; text-align: center; font-family: "Barlow Condensed", sans-serif; font-weight: 700; font-size: 21px; color: var(--ink); }

  .section-title { position: absolute; left: 0; width: 1200px; text-align: center; font-weight: 700; color: var(--ink); }

  .post { position: absolute; top: 1329px; width: 330px; height: 417px; background: var(--white); }
  .post .photo { width: 330px; height: 201px; }
  .post-date { position: absolute; left: 17px; top: 225px; font-size: 14px; font-weight: 600; color: var(--ink); }
  .post-title { position: absolute; left: 17px; top: 259px; font-family: "Barlow Condensed", sans-serif; font-size: 21px; font-weight: 600; color: var(--ink); }
  .post-copy { position: absolute; left: 17px; top: 304px; width: 295px; font-size: 14px; line-height: 18px; color: var(--text); }
  .post-more { position: absolute; left: 17px; top: 375px; font-size: 14px; font-weight: 700; color: var(--ink); display: flex; align-items: center; gap: 6px; }

  .signup-field { position: absolute; left: 233px; top: 1904px; width: 556px; height: 43px; background: var(--white); display: flex; align-items: center; padding-left: 20px; font-size: 16px; color: var(--ink); }
  .signup-field span { margin-left: 30px; }
  .btn-solid { position: absolute; left: 798px; top: 1904px; width: 169px; height: 43px; background: var(--ink); color: var(--white); font-family: "Barlow Condensed", sans-serif; font-weight: 700; font-size: 18px; display: flex; align-items: center; justify-content: center; }

  /* Footer */
  .site-footer { position: absolute; left: 0; top: 2008px; width: 1200px; height: 185px; background: var(--footer); color: var(--white); }
  .footer-links { position: absolute; top: 36px; list-style: none; font-size: 18px; line-height: 33px; letter-spacing: 0.3px; }
  .footer-brand { position: absolute; left: 450px; top: 52px; width: 300px; text-align: center; font-family: "Barlow Condensed", sans-serif; font-weight: 500; }
  .footer-brand .brand-name { font-size: 38px; line-height: 40px; letter-spacing: 1px; }
  .footer-brand .brand-tag { font-size: 17px; line-height: 22px; letter-spacing: 0.8px; }
  .copyright { position: absolute; left: 0; top: 145px; width: 1200px; text-align: center; font-size: 14px; display: flex; justify-content: center; align-items: center; gap: 4px; }
</style>
</head>
<body>

<header class="site-header">
  <div class="brand">
    <div class="brand-name">HOLMWYCK</div>
    <div class="brand-tag">CORVALE'S ONLINE SHOPPING VILLAGE</div>
  </div>
  <div class="search">
    <svg width="16" height="16" viewBox="0 0 16 16"><circle cx="6.5" cy="6.5" r="4.8" fill="none" stroke="#111" stroke-width="2.2"/><line x1="10" y1="10" x2="14.5" y2="14.5" stroke="#111" stroke-width="2.6" stroke-linecap="round"/></svg>
    <span>What are you looking for?</span>
  </div>
  <div class="account">
    <svg width="20" height="22" viewBox="0 0 20 22"><circle cx="10" cy="6.5" r="4.8" fill="none" stroke="#111" stroke-width="1.6"/><path d="M2 21 v-3 a5 5 0 0 1 5 -5 h6 a5 5 0 0 1 5 5 v3 z" fill="none" stroke="#111" stroke-width="1.6"/></svg>
    <span>Sign in or Register</span>
  </div>
  <div class="cart">
    <svg width="22" height="20" viewBox="0 0 22 20"><path d="M0 1.5 h4 l3 11 h11 l3 -8 h-15" fill="none" stroke="#111" stroke-width="2.4" stroke-linejoin="round"/><path d="M6 4.5 h15 l-3 8 h-10 z" fill="#111"/><circle cx="9" cy="17" r="2" fill="#111"/><circle cx="17" cy="17" r="2" fill="#111"/></svg>
    <span>(0)</span>
  </div>
</header>

<nav class="main-nav">
  <a style="left:75px">Home</a>
  <a style="left:166px">About Us</a>
  <a style="left:282px">Products</a>
  <a style="left:400px">Home Delivery</a>
  <a style="left:559px">Contact Us</a>
</nav>

<section class="hero" role="img" aria-label="Assorted rustic bread loaves on a wooden table">
  <div class="hero-panel">
    <div class="hero-title">HOLMWYCK</div>
    <div class="hero-sub">CORVALE'S ONLINE SHOPPING VILLAGE</div>
    <p class="hero-copy">Lorem ipsum dolor sit amet, consectetur adipiscing elit, sed do eiusmod tempor incididunt ut labore et dolore magna aliqua. Ut enim ad minim veniam</p>
    <div class="btn-outline">SHOP NOW</div>
  </div>
  <div class="hero-arrow" style="left:0"><svg width="10" height="12" viewBox="0 0 10 12"><path d="M7 2 L3 6 L7 10" fill="none" stroke="#fff" stroke-width="2.2"/></svg></div>
  <div class="hero-arrow" style="right:0"><svg width="10" height="12" viewBox="0 0 10 12"><path d="M3 2 L7 6 L3 10" fill="none" stroke="#fff" stroke-width="2.2"/></svg></div>
</section>

<div class="brick-wall" role="img" aria-label="White painted brick wall background"></div>

<div class="category" style="left:76px">
  <div class="frame"><div class="photo" role="img" aria-label="Crate of fresh vegetables and fruit" style="background:radial-gradient(circle at 50% 50%, #7a8a3a 0%, #3f5a25 45%, #1d2118 100%)"></div></div>
  <div class="category-label">VILLAGE GROCER</div>
</div>
<div class="category" style="left:437px">
  <div class="frame"><div class="photo" role="img" aria-label="Cuts of raw meat on a dark board" style="background:radial-gradient(circle at 50% 35%, #c98d8a 0%, #7a4a4a 35%, #1a1a1a 80%)"></div></div>
  <div class="category-label">BUTCHERS</div>
</div>
<div class="category" style="left:798px">
  <div class="frame"><div class="photo" role="img" aria-label="Fresh seafood on ice" style="background:radial-gradient(circle at 50% 45%, #c9b4b4 0%, #7e7a86 45%, #3a4252 100%)"></div></div>
  <div class="category-label">SEAFOOD</div>
</div>

<h2 class="section-title" style="top:1240px;font-family:'Barlow Condensed',sans-serif;font-size:40px">RECENT POSTS</h2>

<article class="post" style="left:75px">
  <div class="photo" role="img" aria-label="Fresh vegetables on a dark wooden table" style="background:linear-gradient(135deg, #5b7a35 0%, #c0512e 45%, #d9b93a 70%, #3a3128 100%)"></div>
  <div class="post-date">MAR 8TH 2020</div>
  <h3 class="post-title">FINIBUS BONORUM ET MALORUM</h3>
  <p class="post-copy">Lorem ipsum dolor sit amet, consectetur adipiscing elit, sed do eiusmod tempor incididunt ut labore ...</p>
  <div class="post-more">read more <svg width="7" height="10" viewBox="0 0 7 10"><path d="M1.5 1.5 L5 5 L1.5 8.5" fill="none" stroke="#111" stroke-width="2"/></svg></div>
</article>
<article class="post" style="left:436px">
  <div class="photo" role="img" aria-label="Shelves of preserved food in glass jars" style="background:linear-gradient(180deg, #4a2e1e 0%, #a8772f 40%, #9b3a2a 75%, #5a2a1a 100%)"></div>
  <div class="post-date">MAR 8TH 2020</div>
  <h3 class="post-title">FINIBUS BONORUM ET MALORUM</h3>
  <p class="post-copy">Lorem ipsum dolor sit amet, consectetur adipiscing elit, sed do eiusmod tempor incididunt ut labore ...</p>
  <div class="post-more">read more <svg width="7" height="10" viewBox="0 0 7 10"><path d="M1.5 1.5 L5 5 L1.5 8.5" fill="none" stroke="#111" stroke-width="2"/></svg></div>
</article>
<article class="post" style="left:797px">
  <div class="photo" role="img" aria-label="Cured meats and sausages on a wooden board" style="background:linear-gradient(110deg, #8e2f2f 0%, #c98a80 40%, #a0683c 75%, #7a4a28 100%)"></div>
  <div class="post-date">MAR 8TH 2020</div>
  <h3 class="post-title">FINIBUS BONORUM ET MALORUM</h3>
  <p class="post-copy">Lorem ipsum dolor sit amet, consectetur adipiscing elit, sed do eiusmod tempor incididunt ut labore ...</p>
  <div class="post-more">read more <svg width="7" height="10" viewBox="0 0 7 10"><path d="M1.5 1.5 L5 5 L1.5 8.5" fill="none" stroke="#111" stroke-width="2"/></svg></div>
</article>

<h2 class="section-title" style="top:1818px;font-size:44px">Newsletter Signup</h2>
<div class="signup-field">
  <svg width="18" height="14" viewBox="0 0 18 14"><rect x="1" y="1" width="16" height="12" rx="1.5" fill="none" stroke="#111" stroke-width="1.8"/><path d="M1.5 2 L9 8 L16.5 2" fill="none" stroke="#111" stroke-width="1.8"/></svg>
  <span>Enter Your Email Address</span>
</div>
<div class="btn-solid">SUBSCRIBE</div>

<footer class="site-footer">
  <ul class="footer-links" style="left:95px;top:38px">
    <li>OUR MISSION</li>
    <li>HOME DELIVERY</li>
    <li>CONTACT US</li>
  </ul>
  <div class="footer-brand">
    <div class="brand-name">HOLMWYCK</div>
    <div class="brand-tag">CORVALE'S ONLINE SHOPPING VILLAGE</div>
  </div>
  <ul class="footer-links" style="left:971px;top:28px">
    <li>JOIN THE VILLAGE</li>
    <li>FRIENDWALL</li>
    <li>SNAPGRID</li>
  </ul>
  <div class="copyright">
    <svg width="15" height="15" viewBox="0 0 15 15"><circle cx="7.5" cy="7.5" r="6.3" fill="none" stroke="#fff" stroke-width="1.5"/><path d="M9.8 5.4 A3 3 0 1 0 9.8 9.6" fill="none" stroke="#fff" stroke-width="1.5"/></svg>
    <span>2020 WWW.COMPANYNAME.COM</span>
  </div>
</footer>

</body>
</html>
```